依頼概要
「月見そら堂」は川越の蔵通りに佇み、熟練の和菓子職人がつくる豆菓子を専門に販売しています。創業から70年にわたり、手技による和菓子の技術と希少な地域食材を大切にしながら一粒一粒の豆の美味しさを守っています。
ブランドに関するその他情報やトンマナについては添付資料をご確認ください。

https://tsukimi-soradou.com/

<制作物>
A1ポスター
※採用者には追加で「横断幕」や「展示POP」等の制作を依頼させて頂きます。

<特徴>
①和菓子職人による手技で仕上げた希少な和菓子
②豆にこだわり、100種を超える豆菓子を製造し販売している
③和菓子の町でもある小江戸川越の歴史と文化を受け継いでいる
④「グルテンフリー」または「ローグルテン」の体に優しい菓子

<今施策のターゲット>
①日本文化に対して興味関心の高い「海外モダンラグジュアリー層」
②東南アジアに住む富裕層
③東南アジアで飲食店等を営み「上質で希少な甘味」を求める事業者

<主力商品>
①きなこまめ
月見そら堂の伝統和菓子。完熟空豆を一週間かけて蜜漬けを繰り返したお多福豆。豊潤で濃厚な和菓子の美味しさを味わえる。秩父産の幻の大豆「福寄せ大豆」を使用したきなこが、香ばしさを加える。

<依頼詳細>
海外展示会で使用する「ポスター」の制作をお願いします。
展示会への来場者が外国人となるため、使用する主言語は「英語」としてください。
採用者には

①ポスター
専門店感や多商品感(バラエティー感)の表現を1枚で行うのが難しい場合には、複数数のシリーズ化でのデザイン提案も可(最大5枚の展示が可能)
※基本的には1デザインの制作で問題ありません。

サイズ:A1(縦長)
訴求内容:豆菓子専門店、きなこまめ、伝統的な高級和菓子、グルテンフリー、健康食
シズル感:きなこまめからのシズル感
商品情報等:添付資料(Product)を参照

※その他注意点
ご納品方法:入稿データでの納品としてください。
入稿データのルールやテンプレートは下記URLよりご確認お願いします。

印刷会社 ポスター:ランプレス
https://www.lanpress.jp/lineup/poster

記載項目
ブランド名:Tsukimi Soradou
会社名: Hirata Co., Ltd.
ロゴ:添付ファイル
サイズ(ポスター):A1縦
サイズ(横断幕):幅2100mm 高900mm

添付資料
①Leaflet → ブランドに関する情報やトンマナを確認いただける資料
②Product → ロゴ・写真等の素材
③Others → その他素材
※納品データ制作時に高解像度のデータを提出いたします。

その他にも素材はありますので、必要素材がありましたらお知らせください。

-----追加で依頼をお願いする制作物例----
のぼり横断幕
採用となるデザインパターンは1種のみ。展示可能箇所が1か所のみとなるため、シリーズ化のデザインは不可。

サイズ:幅2100mm 高900mm
生地:テトロンポンジ
シズル感:きなこまめからのシズル感
その他:可能であれば店舗外観を挿入(国内店舗との関連想起を促すため)

海外展示会での使用に対してのバランス感の良さを評価させて頂きました。
また、参考資料とさせていただいたリーフレットとの融和性も高く、海外におけるブランディング構築効果が高いと判断させて頂きました。

ご提案して頂きました皆様、誠にありがとうございます。
選考上での修正につきましても迅速な対応をしていただけたこと、重ねて御礼申し上げます。
最後まで選出に苦慮するほどに素敵なご提案が多く、社員一同感激しております。
別の機会がございましたら、何卒、宜しくお願い致します。

```html
<!DOCTYPE html>
<html lang="en">
<head>
<meta charset="utf-8">
<title>Kinako Mame — Tsukimi Soradou</title>
<link rel="stylesheet" href="https://fonts.googleapis.com/css2?family=EB+Garamond:ital,wght@0,400;1,400&display=swap">
<style>
  :root {
    --paper: #e3eaee;
    --panel: #c9dde7;
    --ink: #2b2b2b;
    --rule: #4a4a4a;
    --kinako-light: #e4cfa6;
    --kinako-deep: #c7a676;
    --bean-light: #3a3440;
    --bean-deep: #121015;
    --ball-light: #f2ede4;
    --ball-deep: #cfc6b6;
  }
  * { margin: 0; padding: 0; box-sizing: border-box; }
  html, body { width: 846px; height: 1200px; overflow: hidden; }
  body {
    background: var(--paper);
    font-family: "EB Garamond", Georgia, serif;
    color: var(--ink);
    position: relative;
  }
  .poster-title {
    position: absolute; top: 14px; left: 0; width: 100%;
    text-align: center; font-style: italic; font-weight: 400;
    font-size: 38px; letter-spacing: 0.5px;
  }
  .panel {
    position: absolute; left: 62px; top: 66px;
    width: 722px; height: 1030px; background: var(--panel);
  }
  .ingredient-label {
    position: absolute; font-style: italic; font-size: 19px;
    transform: translateX(-50%);
  }
  .label-kinako { left: 224px; top: 150px; }
  .label-mame { left: 493px; top: 150px; }
  .leader {
    position: absolute; width: 1px; background: var(--rule);
  }
  .leader-kinako { left: 224px; top: 180px; height: 120px; }
  .leader-mame { left: 493px; top: 180px; height: 105px; }
  .photo-kinako {
    position: absolute; left: 155px; top: 290px; width: 160px; height: 150px;
    border-radius: 50% 50% 46% 46% / 40% 40% 60% 60%;
    background: radial-gradient(ellipse at 50% 45%, var(--kinako-light), var(--kinako-deep) 75%, rgba(199,166,118,0) 100%);
  }
  .photo-mame {
    position: absolute; left: 380px; top: 265px; width: 200px; height: 160px;
    border-radius: 48% 52% 44% 56% / 50% 46% 54% 50%;
    background: radial-gradient(ellipse at 40% 35%, var(--bean-light), var(--bean-deep) 70%);
  }
  .description {
    position: absolute; left: 112px; top: 494px; width: 500px;
    font-style: italic; font-size: 16.5px; line-height: 1.62;
  }
  .arrow { position: absolute; left: 338px; top: 672px; }
  .photo-ball {
    position: absolute; left: 330px; top: 800px; width: 66px; height: 62px;
    border-radius: 50%;
    background: radial-gradient(circle at 40% 35%, var(--ball-light), var(--ball-deep) 85%);
  }
  .product-caption {
    position: absolute; left: 0; top: 906px; width: 100%;
    text-align: center; font-style: italic; font-size: 18px;
    padding-right: 0; transform: translateX(-0px);
  }
  .brand {
    position: absolute; left: 0; top: 1112px; width: 100%;
    display: flex; flex-direction: column; align-items: center; gap: 6px;
  }
  .brand-dot {
    width: 22px; height: 22px; border-radius: 50%;
    border: 1.5px solid var(--ink);
  }
  .brand-name { font-size: 15px; letter-spacing: 1px; }
</style>
</head>
<body>
  <h1 class="poster-title">Kinako Mame</h1>

  <section class="panel">
    <span class="ingredient-label label-kinako">Kinako</span>
    <span class="ingredient-label label-mame">Mame</span>
    <div class="leader leader-kinako"></div>
    <div class="leader leader-mame"></div>

    <div class="photo-kinako" role="img" aria-label="Pile of golden roasted soybean flour (kinako)"></div>
    <div class="photo-mame" role="img" aria-label="Glossy dark honey-soaked otafuku fava beans"></div>

    <p class="description">Traditional Japanese sweets from Tsukimi Soradou. Otafuku beans are made by repeatedly soaking ripe fava beans in honey for a week. You can enjoy the rich and rich taste of Japanese sweets. Kinako, made from Chichibu's phantom soybeans called "fortune-gathering soybeans," adds flavor.</p>

    <svg class="arrow" width="50" height="100" viewBox="0 0 50 100" aria-hidden="true">
      <line x1="25" y1="0" x2="25" y2="96" stroke="#4a4a4a" stroke-width="1.2"/>
      <polyline points="3,74 25,96 47,74" fill="none" stroke="#4a4a4a" stroke-width="1.2"/>
    </svg>

    <div class="photo-ball" role="img" aria-label="A single kinako mame bean coated in pale kinako powder"></div>
    <p class="product-caption">Kinako Mame</p>
  </section>

  <footer class="brand">
    <span class="brand-dot"></span>
    <span class="brand-name">tsukimi soradou</span>
  </footer>
</body>
</html>
```